Bright path Campaign Printable Materials

Design Deliverables:

We request Sketch Harbor to provide the final designs and printable files for both the brochures and election signs, ensuring they adhere to the specifications recommended by InkMeadow.

Print Materials:
- Brochures
- Election Signs

Project Overview:
We are launching a community-centered campaign that prioritizes unity and inclusivity. Rather than focusing on individual candidates, our campaign will embody a collective spirit with the message: “Rally 2 Now: The Bright Path Campaign.” Our aim is to foster trust, transparency, and collaboration by engaging every eligible member of the Moswekan Tebinak Nation in the electoral process.

Election Signs:
No images.
- Version 1: “Rally 2 Now”
Underneath: “Skoden”

- Version 2: “Rally 2 Now”
Underneath: “Stoodis”

Additional Design Notes:
- The design must align with the visuals found on our website.
- Include the flower design.
*See attached files

Brochures:

Main Headline:
“The Bright Path Campaign”

Brochure Content:

Side One:
In the spirit of unity and collaboration, we invite you to join us on a meaningful journey to build a platform that reflects our community's aspirations and values. Every voice matters, and together, we can create a mandate that resonates with the hopes and dreams of all our members. Our vision embraces transparency, open communication, and collaboration, honoring our traditions while embracing progress.

We also extend a warm invitation to other candidates who share our commitment to community growth and well-being. We welcome you to collaborate with us and contribute your unique perspectives as we work toward a common goal.

By investing in cultural revitalization, strengthening Indigenous language programs, and prioritizing sustainable economic development, we aim to cultivate a healthier, more connected community for generations to come. We recognize the importance of healing from the past and are committed to amplifying the voices of our most vulnerable members.

Join us in this vital work. Let’s build a future that honors our heritage and empowers our people. Together, we can create a united community reflecting our shared vision.

We welcome your thoughts, ideas, and participation. Let’s embark on this journey together!

Side Two:
Reach out to one of us at www.rally2now.ca and connect with a team member to share your story and ideas.

Areas of Focus:
- Education
- Families
- Elders
- Youth
- Women
- Men
- Health
- Environmental Responsibility
- Fiscal Responsibility
- Culture
- Language
- Food Sovereignty
- Housing
- Economic Prosperity
- Governance

Contact us at: community@rally2now.ca

Additional Design Notes:
- The design must align with the visuals from our website.
*see attached files

```html
<!DOCTYPE html>
<html lang="en">
<head>
<meta charset="utf-8">
<title>Rally 2 Now – Election Signs</title>
<link rel="stylesheet" href="https://fonts.googleapis.com/css2?family=Anton&display=swap">
<style>
  :root {
    --backdrop: #333333;
    --sign-white: #ffffff;
    --sign-yellow: #ffcc00;
    --ink-blue: #0a28e0;
    --ink-orange: #ff6600;
    --ink-magenta: #ff00ee;
    --petal-pink: #ff22dd;
    --petal-orange: #ff7a00;
    --leaf-green: #00a060;
    --bloom-blue: #1030f0;
  }
  * { margin: 0; padding: 0; box-sizing: border-box; }
  html, body {
    width: 1200px; height: 1200px; overflow: hidden;
    background: var(--backdrop);
  }
  .board { position: relative; width: 1200px; height: 1200px; }
  .sign {
    position: absolute; top: 266px;
    width: 500px; height: 666px; overflow: hidden; display: block;
  }
  .sign--white { left: 65px; }
  .sign--yellow { left: 634px; }
  .sign__ground--white { fill: var(--sign-white); }
  .sign__ground--yellow { fill: var(--sign-yellow); }
  .sign__band { fill: var(--sign-white); }

  .flower--pink { fill: var(--petal-pink); }
  .flower--orange { fill: var(--petal-orange); }
  .flower--blue { fill: var(--bloom-blue); }
  .flower--green { fill: var(--leaf-green); }

  .word {
    font-family: "Anton", "Impact", sans-serif;
    text-transform: uppercase;
  }
  .word--headline { fill: var(--ink-blue); font-size: 232px; }
  .word--bottom { font-size: 224px; }
  .word--slogan { font-size: 99px; }
  .sign--white .word--slogan { fill: var(--ink-orange); }
  .sign--yellow .word--slogan { fill: var(--ink-magenta); }
</style>
</head>
<body>
<main class="board">
  <svg class="sign sign--white" viewBox="0 0 500 666" aria-label="Election sign, white version">
    <rect class="sign__ground--white" width="500" height="666"/>
    <g class="sign__flowers">
      <rect class="flower--blue" x="36" y="0" width="66" height="24" rx="12" role="img" aria-label="Blue floral bloom"/>
      <rect class="flower--orange" x="0" y="20" width="52" height="130" rx="24" role="img" aria-label="Orange floral motif with leaves"/>
      <rect class="flower--pink" x="0" y="205" width="50" height="160" rx="24" role="img" aria-label="Pink floral motif with leaves"/>
      <rect class="flower--pink" x="0" y="605" width="110" height="61" rx="26" role="img" aria-label="Pink floral motif"/>
      <rect class="flower--pink" x="450" y="10" width="50" height="140" rx="24" role="img" aria-label="Pink floral motif with leaf"/>
      <rect class="flower--blue" x="474" y="184" width="26" height="70" rx="13" role="img" aria-label="Blue floral bloom"/>
      <rect class="flower--orange" x="440" y="368" width="60" height="124" rx="28" role="img" aria-label="Orange floral motif with leaves"/>
      <rect class="flower--pink" x="450" y="536" width="50" height="130" rx="24" role="img" aria-label="Pink floral motif with leaf"/>
    </g>
    <text class="word word--headline" x="61" y="266" textLength="376" lengthAdjust="spacingAndGlyphs">Sko</text>
    <text class="word word--slogan" x="77" y="376" textLength="348" lengthAdjust="spacingAndGlyphs">Rally 2 Now</text>
    <text class="word word--headline word--bottom" x="75" y="603" textLength="350" lengthAdjust="spacingAndGlyphs">Den</text>
  </svg>

  <svg class="sign sign--yellow" viewBox="0 0 500 666" aria-label="Election sign, yellow version">
    <rect class="sign__ground--yellow" width="500" height="666"/>
    <rect class="sign__band" x="0" y="276" width="500" height="123"/>
    <g class="sign__flowers">
      <rect class="flower--blue" x="36" y="0" width="66" height="24" rx="12" role="img" aria-label="Blue floral bloom"/>
      <rect class="flower--orange" x="0" y="20" width="52" height="130" rx="24" role="img" aria-label="Orange floral motif with leaves"/>
      <rect class="flower--pink" x="0" y="205" width="50" height="160" rx="24" role="img" aria-label="Pink floral motif with leaves"/>
      <rect class="flower--pink" x="0" y="605" width="110" height="61" rx="26" role="img" aria-label="Pink floral motif"/>
      <rect class="flower--pink" x="450" y="10" width="50" height="140" rx="24" role="img" aria-label="Pink floral motif with leaf"/>
      <rect class="flower--blue" x="474" y="184" width="26" height="70" rx="13" role="img" aria-label="Blue floral bloom"/>
      <rect class="flower--orange" x="440" y="368" width="60" height="124" rx="28" role="img" aria-label="Orange floral motif with leaves"/>
      <rect class="flower--pink" x="450" y="536" width="50" height="130" rx="24" role="img" aria-label="Pink floral motif with leaf"/>
    </g>
    <text class="word word--headline" x="61" y="266" textLength="376" lengthAdjust="spacingAndGlyphs">Sko</text>
    <text class="word word--slogan" x="78" y="380" textLength="348" lengthAdjust="spacingAndGlyphs">Rally 2 Now</text>
    <text class="word word--headline word--bottom" x="76" y="603" textLength="348" lengthAdjust="spacingAndGlyphs">Den</text>
  </svg>
</main>
</body>
</html>
```